Elk R Cellars Wine Label Design

We are looking to redesign our wine labels. i have updated this contest to focus on just the premium wines. These should have gold writing on a silk screened bottle, or on black traditional label. Red or gold capsule.
Our logo is of a mountain with dated cursive script (see attached). We are hoping to maintain some of that brand identity but with a more premium look. The current cursive script definitely needs to be altered. Elk Ridge is an extinct volcano that is a local landmark in the Okanagan Valley. One concept was using this image as a background or element of the labels or a new logo. i have attached an actual photo of the mountain. This is only to inspire a simplified logo.

Target Market(s)

30-65

Logo Text

Elk. (or Elk) Ravensworth

Font styles to use
Serif
Script

Colors
1b1b1b
ec1f27
fbf289

Requirements
Must have
• High End Feel. silkscreen? gold writing. wine is called "Lantern"
Nice to have
• "estate grown"

```html
<!DOCTYPE html>
<html lang="en">
<head>
<meta charset="utf-8">
<title>Lantern — Premium Wine Label</title>
<link rel="stylesheet" href="https://fonts.googleapis.com/css2?family=Cinzel:wght@400;600;700&display=swap">
<style>
  :root {
    --backdrop: #343332;
    --label-black: #1b1b1b;
    --label-deep: #0b0b0b;
    --gold-light: #f3e6a6;
    --gold: #c9a758;
    --gold-dark: #8a6b2c;
    --red: #ec1f27;
    --red-dark: #8e0f14;
  }
  html, body {
    margin: 0;
    padding: 0;
    width: 801px;
    height: 1200px;
    overflow: hidden;
    background: var(--backdrop);
  }
  .canvas {
    position: relative;
    width: 801px;
    height: 1200px;
    background: var(--backdrop);
  }
  .label {
    position: absolute;
    left: 200px;
    top: 35px;
    width: 400px;
    height: 1130px;
    background:
      linear-gradient(180deg, rgba(0,0,0,0) 0%, rgba(0,0,0,0.35) 100%),
      linear-gradient(90deg, var(--label-deep) 0%, var(--label-black) 50%, var(--label-deep) 100%);
  }
  .wine-name {
    position: absolute;
    top: 205px;
    left: 0;
    right: 0;
    margin: 0;
    text-align: center;
    font-family: "Cinzel", serif;
    font-weight: 700;
    font-size: 50px;
    line-height: 60px;
    letter-spacing: 5px;
    padding-left: 5px;
    background: linear-gradient(180deg, var(--gold-light) 0%, var(--gold) 55%, var(--gold-dark) 100%);
    -webkit-background-clip: text;
    background-clip: text;
    color: transparent;
  }
  .landmark-band {
    position: absolute;
    top: 764px;
    left: 0;
    width: 400px;
    height: 122px;
    display: block;
  }
  .vintage {
    position: absolute;
    top: 925px;
    left: 0;
    right: 0;
    margin: 0;
    text-align: center;
    font-family: "Cinzel", serif;
    font-weight: 400;
    font-size: 24px;
    line-height: 30px;
    letter-spacing: 16px;
    padding-left: 16px;
    color: var(--gold);
  }
  .appellation {
    position: absolute;
    top: 968px;
    left: 0;
    right: 0;
    margin: 0;
    text-align: center;
    font-family: "Cinzel", serif;
    font-weight: 400;
    font-size: 15px;
    line-height: 20px;
    letter-spacing: 0.5px;
    color: var(--gold);
  }
</style>
</head>
<body>
  <main class="canvas">
    <section class="label">
      <h1 class="wine-name">LANTERN</h1>
      <svg class="landmark-band" viewBox="0 0 400 122" role="img" aria-label="Gold band with a stylised red mountain silhouette">
        <defs>
          <linearGradient id="band-gold" x1="0" y1="0" x2="1" y2="0">
            <stop offset="0" stop-color="#8a6b2c"/>
            <stop offset="0.5" stop-color="#f3e6a6"/>
            <stop offset="1" stop-color="#8a6b2c"/>
          </linearGradient>
          <linearGradient id="band-red" x1="0" y1="0" x2="1" y2="0">
            <stop offset="0" stop-color="#8e0f14"/>
            <stop offset="0.5" stop-color="#ec1f27"/>
            <stop offset="1" stop-color="#8e0f14"/>
          </linearGradient>
          <linearGradient id="band-fade" x1="0" y1="0" x2="0" y2="1">
            <stop offset="0" stop-color="#1b1b1b" stop-opacity="0.9"/>
            <stop offset="0.5" stop-color="#1b1b1b" stop-opacity="0"/>
          </linearGradient>
        </defs>
        <rect x="0" y="0" width="400" height="70" fill="url(#band-gold)"/>
        <rect x="0" y="55" width="400" height="67" fill="url(#band-red)"/>
        <rect x="0" y="55" width="400" height="67" fill="url(#band-fade)"/>
      </svg>
      <p class="vintage">2016</p>
      <p class="appellation">OKANAGAN VALLEY VQA</p>
    </section>
  </main>
</body>
</html>
```